Kovalen Spinal Care and Performance

We need new business cards, something more modern, clean. On the back of the card maybe a quote. The Dr. likes, “The doctor of the future will give no medicine, but will interest his patient in the care of the human frame, in diet and in the cause and prevention of disease.” - Walter Brisby. We are open to other suggestions. We are a chiropractic office.

```html
<!DOCTYPE html>
<html lang="en">
<head>
<meta charset="UTF-8">
<title>Kovalen Spinal Care and Performance – Business Card</title>
<link href="https://fonts.googleapis.com/css2?family=Questrial&display=swap" rel="stylesheet">
<style>
  :root {
    --purple: #74378a;
    --purple-ink: #6f2f86;
    --white: #ffffff;
    --paper: #fbfbfb;
    --backdrop: #e9e6ea;
  }
  * { margin: 0; padding: 0; box-sizing: border-box; }
  html, body {
    width: 1200px; height: 900px; overflow: hidden;
    background: var(--backdrop);
    font-family: "Questrial", "Century Gothic", sans-serif;
  }
  .canvas {
    position: relative; width: 1200px; height: 900px;
  }
  .card {
    position: absolute; left: 250px; width: 700px; height: 400px;
    box-shadow: 0 6px 18px rgba(0,0,0,0.15);
    overflow: hidden;
  }
  .card--front { top: 40px; background: var(--paper); color: var(--purple-ink); }
  .card--back { top: 470px; background: var(--purple); color: var(--white); text-align: center; }

  /* Front */
  .front__bar {
    position: absolute; left: 18px; top: 46px; width: 16px; height: 320px;
    background: var(--purple); border-radius: 8px 0 0 8px;
  }
  .front__identity { position: absolute; left: 70px; top: 40px; }
  .front__name { font-size: 52px; letter-spacing: 1px; line-height: 1; }
  .front__title { font-size: 26px; margin-left: 88px; margin-top: 6px; letter-spacing: 1px; }
  .front__divider {
    position: absolute; left: 432px; top: 36px; width: 2px; height: 220px;
    background: var(--purple);
  }
  .front__brand {
    position: absolute; left: 452px; top: 92px; width: 230px;
    display: flex; align-items: center; gap: 10px;
    font-size: 17px; line-height: 1.25; color: var(--purple-ink);
  }
  .brand__dot { flex: none; width: 14px; height: 14px; border-radius: 50%; background: var(--purple); }
  .front__contacts { position: absolute; left: 80px; top: 200px; list-style: none; }
  .contact {
    display: flex; align-items: center; gap: 16px;
    height: 36px; font-size: 15px; letter-spacing: 0.5px;
  }
  .contact svg { width: 22px; height: 22px; fill: var(--purple); flex: none; }

  /* Back */
  .back__brand { margin-top: 62px; }
  .back__brand-name { font-size: 68px; letter-spacing: 4px; line-height: 1; }
  .back__brand-line { font-size: 68px; }
  .back__brand-sub { font-size: 24px; letter-spacing: 1px; margin-top: 8px; }
  .back__rule {
    width: 440px; height: 2px; background: var(--white); margin: 18px auto 0; border-radius: 1px;
  }
  .back__quote {
    font-size: 18px; line-height: 1.35; letter-spacing: 0.4px;
    width: 600px; margin: 22px auto 0;
  }
  .back__web { position: absolute; left: 0; right: 0; bottom: 30px; font-size: 22px; letter-spacing: 1.5px; }
</style>
</head>
<body>
<main class="canvas">

  <section class="card card--front" aria-label="Card front">
    <div class="front__bar"></div>
    <div class="front__identity">
      <h1 class="front__name">Marcus Hale</h1>
      <p class="front__title">General Manager</p>
    </div>
    <div class="front__divider"></div>
    <div class="front__brand">
      <span class="brand__dot"></span>
      <span>Kovalen Spinal Care &amp; Performance</span>
    </div>
    <ul class="front__contacts">
      <li class="contact">
        <svg viewBox="0 0 24 24" aria-hidden="true"><path d="M6.6 10.8c1.4 2.8 3.8 5.2 6.6 6.6l2.2-2.2c.3-.3.7-.4 1-.2 1.1.4 2.3.6 3.6.6.6 0 1 .4 1 1V20c0 .6-.4 1-1 1C10.6 21 3 13.4 3 4c0-.6.4-1 1-1h3.5c.6 0 1 .4 1 1 0 1.3.2 2.5.6 3.6.1.3 0 .7-.2 1z"/></svg>
        <span>+12 555 0148</span>
      </li>
      <li class="contact">
        <svg viewBox="0 0 24 24" aria-hidden="true"><path d="M12 2a7 7 0 0 0-7 7c0 5.2 7 13 7 13s7-7.8 7-13a7 7 0 0 0-7-7zm0 9.5A2.5 2.5 0 1 1 12 6.5a2.5 2.5 0 0 1 0 5z"/></svg>
        <span>Street Name, City, Country</span>
      </li>
      <li class="contact">
        <svg viewBox="0 0 24 24" aria-hidden="true"><path d="M3 5h18v14H3zm2 2v.4l7 4.6 7-4.6V7zm0 2.8V17h14V9.8l-7 4.6z"/></svg>
        <span>marcus.hale@kovalenspine.com</span>
      </li>
      <li class="contact">
        <svg viewBox="0 0 24 24" aria-hidden="true"><path d="M5 3l14 7-6 1.8 4.5 6.2-2.4 1.8-4.5-6.2L6.5 18z"/></svg>
        <span>www.kovalenspine.com</span>
      </li>
    </ul>
  </section>

  <section class="card card--back" aria-label="Card back">
    <div class="back__brand">
      <p class="back__brand-name">KOVALEN</p>
      <p class="back__brand-sub">SPINAL CARE &amp; PERFORMANCE</p>
    </div>
    <div class="back__rule"></div>
    <blockquote class="back__quote">
      “The doctor of the future will give no medicine, but will interest his patient in the care of the human frame, in diet and in the cause and prevention of disease.” - Walter Brisby
    </blockquote>
    <p class="back__web">www.kovalenspine.com</p>
  </section>

</main>
</body>
</html>
```